Brochure design for 3D ultrasound company

I am looking for a clean and modern and edgy brochure for my ultrasound company. We are a fairly new company specialize in 3D/4D ultrasounds.Our brochures will be placed in OB-GYN offices in high end areas around Los Angeles, so we need something that will stand out and capture a modern woman's attention. Our logo is currently in the process of being designed, so I don't have a picture to provide quite yet, however it will be our company name"Kite + Lantern" written in a special font that looks like neon lights. I will attach a few images of what our logo will be like, and some initial content that can help provide the layout we would like for the brochure. please feel free to also take a look at our website. www.kitelanternscan.example.

Target Market(s)

Upscale trendy women.

Colors
eea4c8
33a6d7
fee18a

Requirements
Should not have
• too many colors.

```html
<!DOCTYPE html>
<html lang="en">
<head>
<meta charset="utf-8">
<title>Kite + Lantern — Tri-fold Brochure, Outside</title>
<link href="https://fonts.googleapis.com/css2?family=Josefin+Sans:wght@400;600;700&family=Montserrat:wght@700;800;900&family=Playfair+Display:ital@1&display=swap" rel="stylesheet">
<style>
:root{
  --page:#d4d4d5;
  --paper:#f1f1f1;
  --ink:#262626;
  --night:#0f0a0b;
  --blush:#f2979a;
  --blush-deep:#ef8c90;
  --light:#ffffff;
  --skin:#d9a383;
}
*{box-sizing:border-box;margin:0;padding:0}
html,body{width:833px;height:1200px;overflow:hidden;background:var(--page)}
body{position:relative;font-family:"Josefin Sans",sans-serif;color:var(--ink)}

.side-label{position:absolute;right:66px;top:28px;font:900 22px "Montserrat",sans-serif;color:#b9b9ba;letter-spacing:.5px}

.row-single{position:absolute;left:0;top:67px;width:833px}
.row-single .panel{position:absolute;top:0;transform:scale(.875);transform-origin:0 0;box-shadow:0 2px 6px rgba(0,0,0,.25)}
.row-single .p1{left:65px}
.row-single .p2{left:311px;top:4px}
.row-single .p3{left:560px}

.spread{position:absolute;left:67px;top:613px;width:696px;height:532px;display:flex;box-shadow:0 3px 8px rgba(0,0,0,.25)}
.spread .panel{position:relative}

.panel{width:232px;height:532px;position:absolute;overflow:hidden;background:var(--paper)}
.panel svg.shape{position:absolute;left:0;top:0}

/* company name, set in the body face */
.wordmark{position:absolute;width:100%;text-align:center;font:700 24px "Josefin Sans",sans-serif;color:var(--light)}

/* cover */
.cover-photo{position:absolute;left:0;top:0;width:232px;height:400px;
  background:linear-gradient(180deg,#f4f3f2 0%,#eeebe8 30%,#d9cfc8 55%,#c9c7cc 72%,#e6e4e4 100%)}
.cover-kicker{position:absolute;top:24px;width:100%;text-align:center;font-size:11.5px}
.cover-title{position:absolute;top:40px;width:100%;text-align:center;font:800 19px/22px "Montserrat",sans-serif;color:var(--blush);text-transform:uppercase}
.cover .wordmark{top:424px}
.call{position:absolute;top:470px;width:100%;text-align:center;font:italic 13px "Playfair Display",serif;color:#fff}
.phone-tab{position:absolute;left:22px;bottom:0;width:188px;height:33px;background:#f2f2f2;border-radius:6px 6px 0 0;
  display:flex;align-items:center;justify-content:center;gap:4px;font:800 15px "Montserrat",sans-serif;color:#1a1a1a}

/* about + contact */
.about{position:absolute;top:26px;left:26px;right:26px;text-align:center;color:#fff;font-size:9.4px;line-height:12px}
.about p+p{margin-top:12px}
.about b{font-weight:700}
.about-panel .wordmark{top:170px;font-size:22px}
.map{position:absolute;left:52px;top:219px;width:136px;height:136px;border-radius:50%;
  background:radial-gradient(circle at 45% 40%,#f2eee3 0%,#ece4cf 55%,#e4d2a8 80%,#cfe0ef 100%);border:5px solid #f3f3f3;box-shadow:0 0 0 3px var(--blush)}
.contact-title{position:absolute;top:370px;width:100%;text-align:center;font:800 13px "Montserrat",sans-serif}
.rule{position:absolute;left:50%;width:24px;height:1.5px;background:var(--ink);transform:translateX(-50%)}
.contact-panel-rule{top:390px}
.icons{position:absolute;top:398px;width:100%;display:flex;justify-content:center;gap:12px}
.icon{width:14px;height:14px;border-radius:50%;background:#f8dcdc;display:flex;align-items:center;justify-content:center}
.contact-list{position:absolute;top:418px;width:100%;text-align:center;font-size:9.6px;line-height:13.6px;font-weight:600}

/* what's what */
.mark-dot{position:absolute;left:111px;top:30px;width:10px;height:10px;border-radius:50%;background:var(--blush)}
.whats-title{position:absolute;top:60px;width:100%;text-align:center;font:800 13px "Montserrat",sans-serif}
.whats-rule{top:84px}
.glossary{position:absolute;top:100px;left:17px;right:17px;font-size:9px;line-height:12px;text-align:justify}
.glossary p+p{margin-top:11px}
.glossary b{font-weight:700}
.belly-photo{position:absolute;left:0;top:330px;width:232px;height:202px;
  background:radial-gradient(ellipse at 50% 60%,#e3b595 0%,var(--skin) 45%,#b98367 75%,#3b3333 100%)}
</style>
</head>
<body>

<div class="side-label">OUTSIDE</div>

<div class="row-single">
  <section class="panel cover p1">
    <div class="cover-photo" role="img" aria-label="Photo of a smiling pregnant woman in a white top sitting on a bed, holding an ultrasound print strip up over her eyes"></div>
    <svg class="shape" width="232" height="532" viewBox="0 0 232 532">
      <path d="M0 356 Q116 386 232 350 L232 532 L0 532Z" fill="var(--blush)"/>
      <path d="M0 366 Q116 398 232 360 L232 532 L0 532Z" fill="var(--night)"/>
    </svg>
    <p class="cover-kicker">A mobile 3D/4D ultrasound service</p>
    <h1 class="cover-title">Ultrasound in<br>the comfort of<br>your home</h1>
    <p class="wordmark">Kite + Lantern</p>
    <p class="call">Call Today!</p>
    <div class="phone-tab"><svg width="13" height="13" viewBox="0 0 24 24"><path d="M6.6 10.8a15 15 0 006.6 6.6l2.2-2.2c.3-.3.7-.4 1-.2 1.1.4 2.3.6 3.6.6.6 0 1 .4 1 1V20c0 .6-.4 1-1 1C10.6 21 3 13.4 3 4c0-.6.4-1 1-1h3.5c.6 0 1 .4 1 1 0 1.3.2 2.5.6 3.6.1.3 0 .7-.2 1z" fill="#1a1a1a"/></svg>555-014-2290</div>
  </section>

  <section class="panel about-panel p2">
    <svg class="shape" width="232" height="532" viewBox="0 0 232 532">
      <path d="M0 0H232V370Q150 318 80 262Q30 222 0 168Z" fill="var(--blush)"/>
      <path d="M0 0H232V358Q150 306 80 252Q32 214 0 156Z" fill="var(--night)"/>
      <path d="M0 420Q10 490 40 532H33Q5 492 0 440Z" fill="var(--blush)"/>
    </svg>
    <div class="about">
      <p><b>Kite + Lantern</b> is a mobile 3D ultrasound company servicing Los Angeles, and surrounding areas. We take great pride in being one of LA’s first mobile Ultrasound companies and for being an all female business!</p>
      <p>Our mission is to provide an unforgettable experience for expectant mothers in the comfort of their home!</p>
    </div>
    <p class="wordmark">Kite + Lantern</p>
    <div class="map" role="img" aria-label="Street map of Los Angeles and surrounding service area"></div>
    <h2 class="contact-title">Contact Us</h2>
    <span class="rule contact-panel-rule"></span>
    <div class="icons">
      <span class="icon"><svg width="8" height="8" viewBox="0 0 24 24"><path d="M6.6 10.8a15 15 0 006.6 6.6l2.2-2.2c.3-.3.7-.4 1-.2 1.1.4 2.3.6 3.6.6.6 0 1 .4 1 1V20c0 .6-.4 1-1 1C10.6 21 3 13.4 3 4c0-.6.4-1 1-1h3.5c.6 0 1 .4 1 1 0 1.3.2 2.5.6 3.6.1.3 0 .7-.2 1z" fill="var(--blush-deep)"/></svg></span>
      <span class="icon"></span>
      <span class="icon"><svg width="9" height="7" viewBox="0 0 18 14"><rect x="1" y="1" width="16" height="12" fill="none" stroke="var(--blush-deep)" stroke-width="2"/><path d="M1 1l8 7 8-7" fill="none" stroke="var(--blush-deep)" stroke-width="2"/></svg></span>
      <span class="icon"></span>
      <span class="icon"></span>
    </div>
    <div class="contact-list">
      <p>Telephone: (555) 014-2290</p>
      <p>www.kitelanternscan.example</p>
      <p>Email: info@kitelanternscan.example</p>
      <p>Instagram: kite_lantern</p>
      <p>Facebook: @kitelanternscan</p>
    </div>
  </section>

  <section class="panel whats p3">
    <div class="belly-photo" role="img" aria-label="Close-up of a pregnant belly with hands holding a 3D ultrasound print"></div>
    <svg class="shape" width="232" height="532" viewBox="0 0 232 532">
      <path d="M0 322Q150 310 232 420V434Q150 322 0 334Z" fill="var(--blush)"/>
      <path d="M0 0H232V420Q150 310 0 322Z" fill="var(--paper)"/>
    </svg>
    <span class="mark-dot"></span>
    <h2 class="whats-title">WHAT’S WHAT...</h2>
    <span class="rule whats-rule"></span>
    <div class="glossary">
      <p><b>2D</b> is the traditional black and white photo— you know, the one that you want to get emotional about, but you don’t know what you’re looking at.</p>
      <p><b>3D</b> is an image of the fetus and it’s features. So you can see the baby has dad’s nose, and mom’s lips.</p>
      <p><b>4D</b> is 3D, but with motion. You can see the baby yawn, move it’s arm, or even give you a smile.</p>
      <p><b>HD</b> is also 3D, but better. Now you can see a rendering of the baby’s skin making it the most realistic fetal image possible..</p>
      <p>we are one of the few in Los Angeles that have the newest HD capable machines</p>
    </div>
  </section>
</div>

<div class="spread">
  <section class="panel whats">
    <div class="belly-photo" role="img" aria-label="Close-up of a pregnant belly with hands holding a 3D ultrasound print"></div>
    <svg class="shape" width="232" height="532" viewBox="0 0 232 532">
      <path d="M0 322Q150 310 232 420V434Q150 322 0 334Z" fill="var(--blush)"/>
      <path d="M0 0H232V420Q150 310 0 322Z" fill="var(--paper)"/>
    </svg>
    <span class="mark-dot"></span>
    <h2 class="whats-title">WHAT’S WHAT...</h2>
    <span class="rule whats-rule"></span>
    <div class="glossary">
      <p><b>2D</b> is the traditional black and white photo— you know, the one that you want to get emotional about, but you don’t know what you’re looking at.</p>
      <p><b>3D</b> is an image of the fetus and it’s features. So you can see the baby has dad’s nose, and mom’s lips.</p>
      <p><b>4D</b> is 3D, but with motion. You can see the baby yawn, move it’s arm, or even give you a smile.</p>
      <p><b>HD</b> is also 3D, but better. Now you can see a rendering of the baby’s skin making it the most realistic fetal image possible..</p>
      <p>we are one of the few in Los Angeles that have the newest HD capable machines</p>
    </div>
  </section>

  <section class="panel about-panel">
    <svg class="shape" width="232" height="532" viewBox="0 0 232 532">
      <path d="M0 0H232V370Q150 318 80 262Q30 222 0 168Z" fill="var(--blush)"/>
      <path d="M0 0H232V358Q150 306 80 252Q32 214 0 156Z" fill="var(--night)"/>
      <path d="M0 420Q10 490 40 532H33Q5 492 0 440Z" fill="var(--blush)"/>
    </svg>
    <div class="about">
      <p><b>Kite + Lantern</b> is a mobile 3D ultrasound company servicing Los Angeles, and surrounding areas. We take great pride in being one of LA’s first mobile Ultrasound companies and for being an all female business!</p>
      <p>Our mission is to provide an unforgettable experience for expectant mothers in the comfort of their home!</p>
    </div>
    <p class="wordmark">Kite + Lantern</p>
    <div class="map" role="img" aria-label="Street map of Los Angeles and surrounding service area"></div>
    <h2 class="contact-title">Contact Us</h2>
    <span class="rule contact-panel-rule"></span>
    <div class="icons">
      <span class="icon"><svg width="8" height="8" viewBox="0 0 24 24"><path d="M6.6 10.8a15 15 0 006.6 6.6l2.2-2.2c.3-.3.7-.4 1-.2 1.1.4 2.3.6 3.6.6.6 0 1 .4 1 1V20c0 .6-.4 1-1 1C10.6 21 3 13.4 3 4c0-.6.4-1 1-1h3.5c.6 0 1 .4 1 1 0 1.3.2 2.5.6 3.6.1.3 0 .7-.2 1z" fill="var(--blush-deep)"/></svg></span>
      <span class="icon"></span>
      <span class="icon"><svg width="9" height="7" viewBox="0 0 18 14"><rect x="1" y="1" width="16" height="12" fill="none" stroke="var(--blush-deep)" stroke-width="2"/><path d="M1 1l8 7 8-7" fill="none" stroke="var(--blush-deep)" stroke-width="2"/></svg></span>
      <span class="icon"></span>
      <span class="icon"></span>
    </div>
    <div class="contact-list">
      <p>Telephone: (555) 014-2290</p>
      <p>www.kitelanternscan.example</p>
      <p>Email: info@kitelanternscan.example</p>
      <p>Instagram: kite_lantern</p>
      <p>Facebook: @kitelanternscan</p>
    </div>
  </section>

  <section class="panel cover">
    <div class="cover-photo" role="img" aria-label="Photo of a smiling pregnant woman in a white top sitting on a bed, holding an ultrasound print strip up over her eyes"></div>
    <svg class="shape" width="232" height="532" viewBox="0 0 232 532">
      <path d="M0 356 Q116 386 232 350 L232 532 L0 532Z" fill="var(--blush)"/>
      <path d="M0 366 Q116 398 232 360 L232 532 L0 532Z" fill="var(--night)"/>
    </svg>
    <p class="cover-kicker">A mobile 3D/4D ultrasound service</p>
    <h1 class="cover-title">Ultrasound in<br>the comfort of<br>your home</h1>
    <p class="wordmark">Kite + Lantern</p>
    <p class="call">Call Today!</p>
    <div class="phone-tab"><svg width="13" height="13" viewBox="0 0 24 24"><path d="M6.6 10.8a15 15 0 006.6 6.6l2.2-2.2c.3-.3.7-.4 1-.2 1.1.4 2.3.6 3.6.6.6 0 1 .4 1 1V20c0 .6-.4 1-1 1C10.6 21 3 13.4 3 4c0-.6.4-1 1-1h3.5c.6 0 1 .4 1 1 0 1.3.2 2.5.6 3.6.1.3 0 .7-.2 1z" fill="#1a1a1a"/></svg>555-014-2290</div>
  </section>
</div>

</body>
</html>
```